Need new sign at entrance for new fruit and vegetable wholesaler in market. Main vegetables sold are
Broccoli , Cauliflower , cabbage , capsicum , tomatoes , lettuce .
Business name is Tall Meadow
I have included examples of other designs and a sketch of suggested layout.

```html
<!DOCTYPE html>
<html lang="en">
<head>
<meta charset="utf-8">
<title>Tall Meadow – Entrance Sign</title>
<link href="https://fonts.googleapis.com/css2?family=Fira+Sans+Condensed:wght@400&display=swap" rel="stylesheet">
<style>
  :root {
    --page: #ffffff;
    --olive: #7f8c2b;
    --lime: #a9d038;
    --ink: #ffffff;
    --produce-red: #9b2f35;
    --produce-green: #4f8a1f;
  }
  html, body {
    margin: 0;
    padding: 0;
    width: 1200px;
    height: 1000px;
    overflow: hidden;
    background: var(--page);
  }
  .canvas {
    position: relative;
    width: 1200px;
    height: 1000px;
    font-family: "Fira Sans Condensed", "Arial Narrow", sans-serif;
    font-weight: 400;
    color: var(--ink);
  }
  .sign {
    position: absolute;
    left: 0;
    top: 393px;
    width: 1200px;
    height: 217px;
    overflow: hidden;
    background: var(--olive);
  }
  .backdrop {
    position: absolute;
    inset: 0;
    background: radial-gradient(ellipse 70% 120% at 50% 45%, var(--lime) 0%, #95b033 45%, var(--olive) 100%);
  }
  .wordmark {
    position: absolute;
    left: 420px;
    top: 4px;
    width: 360px;
    margin: 0;
    font-weight: 400;
    text-align: center;
    line-height: 0.92;
    text-transform: uppercase;
  }
  .wordmark .line-top { display: block; font-size: 96px; letter-spacing: 1px; }
  .wordmark .line-bottom { display: block; font-size: 72px; }
  .produce {
    position: absolute;
    left: 488px;
    top: 180px;
    width: 230px;
    height: 37px;
    background: linear-gradient(90deg, var(--produce-red), var(--produce-green) 50%, var(--produce-red));
  }
  .location {
    position: absolute;
    left: 24px;
    top: 136px;
    font-size: 29px;
    line-height: 30px;
    text-transform: uppercase;
  }
  .contact {
    position: absolute;
    right: 28px;
    top: 108px;
    font-size: 26px;
    line-height: 30px;
    text-align: right;
  }
  .location p, .contact p { margin: 0; }
</style>
</head>
<body>
<div class="canvas">
  <section class="sign">
    <div class="backdrop" role="img" aria-label="Green sunburst rays radiating from the centre of the sign"></div>

    <h1 class="wordmark">
      <span class="line-top">Tall</span>
      <span class="line-bottom">Meadow</span>
    </h1>

    <div class="produce" role="img" aria-label="Row of fresh tomatoes, broccoli and capsicum"></div>

    <div class="location">
      <p>Stand 47</p>
      <p>C Shed</p>
    </div>

    <div class="contact">
      <p>www.tallmeadow.com.au</p>
      <p>Phone - 02 5550 4821</p>
      <p>Fax - 02 5550 4822</p>
    </div>
  </section>
</div>
</body>
</html>
```